Seasonal Produce Calender Design

Design a seasonal fruit and vegetable calender made ready to print in various sizes. fruits and vegetables to be categorised into moths they are in season. File provided with content. Design is to flow with current company Logo, colours and brand identity. Can provide designers with link to similar calenders.

Please see link this is what im after:

https://www.harlowbrant.com.au/wp-content/uploads/2018/07/Seasonal-Calendar-Alts.jpg

Font styles to use
Serif

Colors

Designer to choose colors to be used in the design.

```html
<!DOCTYPE html>
<html lang="en">
<head>
<meta charset="utf-8">
<title>Seasonal Vegetable &amp; Fruit Calendar</title>
<link rel="stylesheet" href="https://fonts.googleapis.com/css2?family=Anton&family=Bebas+Neue&family=Montserrat:wght@600;700&family=Open+Sans:wght@400;600&display=swap">
<style>
  :root {
    --ink: #111111;
    --text: #2a2a2a;
    --paper: #ffffff;
    --yellow: #fbd535;
    --mint: #d9eee2;
    --cream: #fdf0d2;
    --summer-red: #c4262e;
    --autumn-black: #111111;
    --winter-green: #8cc63f;
    --spring-wine: #9d1f25;
  }
  * { box-sizing: border-box; }
  html, body {
    margin: 0; width: 1200px; height: 4909px; overflow: hidden;
    background: var(--paper); color: var(--text);
    font-family: "Open Sans", Arial, sans-serif;
  }
  .calendar { position: relative; width: 1200px; height: 4909px; }
  .masthead { position: absolute; left: 0; top: 0; width: 1200px; height: 1030px; background: var(--ink); }
  .sheet { position: absolute; left: 53px; top: 895px; width: 1094px; height: 4014px; background: var(--paper); }
  .hero-produce {
    position: absolute; left: 257px; top: 95px; width: 638px; height: 324px; border-radius: 50% 50% 40% 40%;
    background: radial-gradient(ellipse at 30% 55%, #f28a1e 0%, #e9a23b 30%, transparent 55%),
                radial-gradient(ellipse at 70% 45%, #d3321f 0%, #ecc21f 35%, transparent 60%),
                linear-gradient(90deg, #6fae3a, #f0c22b, #d3321f);
    opacity: .9;
  }
  .brand-name {
    position: absolute; left: 0; top: 430px; width: 1200px; text-align: center;
    font-family: "Montserrat", sans-serif; font-weight: 700; color: var(--yellow);
    font-size: 72px; line-height: 1.05; letter-spacing: 10px; text-transform: uppercase; margin: 0;
  }
  .calendar-title { position: absolute; left: 57px; top: 806px; width: 1082px; height: 84px; }
  .calendar-title text { font-family: "Bebas Neue", sans-serif; fill: var(--paper); font-size: 96px; }

  /* stacking: photos sit behind type and panels */
  .produce { position: absolute; border-radius: 45%; z-index: 1; }
  .season-word { position: absolute; z-index: 2; }
  .box { position: absolute; z-index: 3; }
  .month { z-index: 4; }

  .season-word text { font-family: "Anton", sans-serif; fill: var(--yellow); font-size: 292px; }

  .month {
    position: absolute; display: flex; align-items: center; justify-content: center;
    writing-mode: vertical-rl; color: var(--paper);
    font-family: "Montserrat", sans-serif; font-weight: 700; font-size: 21px; letter-spacing: 2px; text-transform: uppercase;
  }
  .month--up { transform: rotate(180deg); }
  .month--summer { background: var(--summer-red); }
  .month--autumn { background: var(--autumn-black); }
  .month--winter { background: var(--winter-green); color: var(--ink); }
  .month--spring { background: var(--spring-wine); }

  .box--mint { background: var(--mint); }
  .box--cream { background: var(--cream); }
  .box-title {
    position: absolute; left: 14px; top: 22px; margin: 0;
    writing-mode: vertical-rl; transform: rotate(180deg);
    font-family: "Montserrat", sans-serif; font-weight: 700; font-size: 26px; letter-spacing: 6px;
    color: var(--ink); text-transform: uppercase; white-space: nowrap;
  }
  .box-title--tight { font-size: 21px; letter-spacing: 1px; }
  .items { position: absolute; margin: 0; padding: 0; list-style: none; font-size: var(--fs); }
  .items li { line-height: var(--lh); margin-bottom: var(--gap); white-space: nowrap; }

  .season--summer { --fs: 16px; --lh: 18.4px; --gap: 6.5px; }
  .season--autumn { --fs: 15px; --lh: 17px; --gap: 4.9px; }
  .season--winter { --fs: 17px; --lh: 19.5px; --gap: 7.4px; }
  .season--spring { --fs: 15px; --lh: 17px; --gap: 6.2px; }
  .items--roomy { --fs: 19px; --lh: 22px; --gap: 11px; }
  .items--herbs-spring { --lh: 18px; --gap: 9px; }

  .veg--autumn { clip-path: polygon(0 0, 100% 0, 100% 333px, 229px 333px, 229px 100%, 0 100%); }
  .veg--winter { clip-path: polygon(0 0, 100% 0, 100% 410px, 238px 410px, 238px 100%, 0 100%); }
  .veg--spring { clip-path: polygon(0 0, 100% 0, 100% 324px, 239px 324px, 239px 100%, 0 100%); }

  .produce--potato { background: radial-gradient(ellipse, #e6c98c 0%, #d9b06a 55%, transparent 72%); }
  .produce--lettuce { background: radial-gradient(ellipse, #9bd24a 0%, #6fae2e 55%, transparent 72%); }
  .produce--tomato { background: radial-gradient(ellipse, #e0382a 0%, #c62a20 50%, transparent 72%); }
  .produce--orange { background: radial-gradient(ellipse, #f7922a 0%, #ea7a16 55%, transparent 72%); }
  .produce--onion { background: radial-gradient(ellipse, #e0a861 0%, #c58842 55%, transparent 72%); }
  .produce--broccoli { background: radial-gradient(ellipse, #5f9e34 0%, #3f7d25 55%, transparent 72%); }
  .produce--beet { background: radial-gradient(ellipse, #7a1e3a 0%, #5c1429 50%, #6fa13b 62%, transparent 75%); }
  .produce--chilli { background: radial-gradient(ellipse, #d12a1f 0%, #b01d16 50%, transparent 72%); }
  .produce--cherry { background: radial-gradient(ellipse, #b3121d 0%, #8c0c15 50%, transparent 72%); }

  .footer-url {
    position: absolute; left: 105px; top: 4826px; margin: 0;
    font-family: "Anton", sans-serif; font-size: 44px; letter-spacing: 7px; color: var(--ink);
  }
  .social { position: absolute; right: 60px; top: 4815px; text-align: right; font-size: 17px; color: var(--ink); font-weight: 600; line-height: 30px; z-index: 5; }
  .social-dot { display: inline-block; width: 20px; height: 20px; border-radius: 50%; background: var(--summer-red); vertical-align: -4px; margin-left: 10px; }
</style>
</head>
<body>
<main class="calendar">
  <header class="masthead">
    <div class="hero-produce" role="img" aria-label="Illustrated cluster of fresh fruit and vegetables"></div>
    <p class="brand-name">The Crisp<br>Harvest Co</p>
    <svg class="calendar-title" viewBox="0 0 1082 84" aria-label="Seasonal Vegetable &amp; Fruit Calendar">
      <text x="0" y="80" textLength="1082" lengthAdjust="spacingAndGlyphs">SEASONAL VEGETABLE &amp; FRUIT CALENDAR</text>
    </svg>
  </header>
  <div class="sheet"></div>

  <!-- Summer -->
  <section class="season season--summer">
    <svg class="season-word" style="left:86px;top:933px" width="219" height="801" aria-label="Summer">
      <text transform="rotate(-90)" x="-801" y="213" textLength="801" lengthAdjust="spacingAndGlyphs">SUMMER</text>
    </svg>
    <div class="month month--summer month--up" style="left:171px;top:952px;width:42px;height:153px">December</div>
    <div class="month month--summer month--up" style="left:171px;top:1238px;width:42px;height:162px">January</div>
    <div class="month month--summer month--up" style="left:171px;top:1562px;width:42px;height:162px">Febuary</div>

    <div class="box box--mint" style="left:358px;top:939px;width:236px;height:791px">
      <h2 class="box-title">Fruits</h2>
      <ul class="items" style="left:69px;top:31px">
        <li>Apricot</li><li>Banana</li><li>Blackberries</li><li>Blueberries</li><li>Boysenberries</li><li>Cantaloupe</li><li>Cherries</li><li>Currants</li><li>Fig</li><li>Grapefruit</li><li>Grapes</li><li>Honeydew</li><li>Lemon</li><li>Loganberries</li><li>Lychee</li><li>Mango</li><li>Mulberries</li><li>Nectarine</li><li>Orange Valencia</li><li>Passionfruit</li><li>Peach</li><li>Plum</li><li>Pineapple</li><li>Rambutan</li><li>Raspberries</li><li>Rhubarb</li><li>Strawberries</li><li>Tamarillo</li><li>Watermelon</li>
      </ul>
    </div>
    <div class="box box--cream" style="left:613px;top:939px;width:248px;height:791px">
      <h2 class="box-title">Vegetables</h2>
      <ul class="items" style="left:69px;top:31px">
        <li>Asparagus</li><li>Avocado</li><li>Beans<br>(Butter, Green)</li><li>Beetroot</li><li>Cabbage</li><li>Capsicum</li><li>Carrot</li><li>Celery</li><li>Corn</li><li>Cucumber</li><li>Daikon</li><li>Eggplant</li><li>Leek</li><li>Lettuce</li><li>Okra</li><li>Onion</li><li>Onion, Spring</li><li>Peas</li><li>Potato</li><li>Radish</li><li>Shallot</li><li>Silverbeet</li><li>Snow Peas</li><li>Squash</li><li>Sugarsnaps</li><li>Tomato</li><li>Watercress</li><li>Zucchini</li><li>Zucchini Flower</li>
      </ul>
    </div>
    <div class="box box--mint" style="left:872px;top:939px;width:232px;height:518px">
      <h2 class="box-title">Herbs &amp; Spices</h2>
      <ul class="items" style="left:69px;top:31px">
        <li>Basil</li><li>Chervil</li><li>Chilli</li><li>Chives</li><li>Coriander</li><li>Dill</li><li>Garlic</li><li>Ginger</li><li>Lime, Kaffir<br>(Leaves)</li><li>Lemongrass</li><li>Mint</li><li>Oregano</li><li>Parsley</li><li>Rosemary</li><li>Sage</li><li>Tarragon</li><li>Thyme</li>
      </ul>
    </div>
    <div class="produce produce--potato" style="left:67px;top:1772px;width:295px;height:200px" role="img" aria-label="Photo of washed potatoes"></div>
    <div class="produce produce--lettuce" style="left:676px;top:1680px;width:448px;height:300px" role="img" aria-label="Photo of a green lettuce head"></div>
  </section>

  <!-- Autumn -->
  <section class="season season--autumn">
    <div class="box box--mint" style="left:86px;top:1991px;width:248px;height:771px">
      <h2 class="box-title">Fruits</h2>
      <ul class="items" style="left:66px;top:21px">
        <li>Avocado</li><li>Blackberries</li><li>Banana</li><li>Cumquat</li><li>Custard Apple</li><li>Fig</li><li>Grapefruit</li><li>Grapes</li><li>Guava</li><li>Honeydew</li><li>Kiwi Fruit</li><li>Lemon</li><li>Lime</li><li>Mandarin Imperial</li><li>Mango</li><li>Mangosteen</li><li>Nashi</li><li>Orange<br>(Navel, Valencia)</li><li>Papaya</li><li>Passionfruit</li><li>Peach</li><li>Pear Nashi</li><li>Persimmon</li><li>Plum</li><li>Pomegranate</li><li>Prickly Pear</li><li>Quince</li><li>Rambutan</li><li>Raspberries</li><li>Rhubarb</li><li>Rockmelon</li><li>Strawberries</li><li>Tamarillo</li>
      </ul>
    </div>
    <div class="box box--cream veg--autumn" style="left:352px;top:1991px;width:467px;height:771px">
      <h2 class="box-title box-title--tight">Vegetables</h2>
      <ul class="items" style="left:63px;top:30px">
        <li>Artichoke Jerusalem</li><li>Asian Greens<br>(Bok Choy, Choysum,<br>Gailan, Wombok)</li><li>Avocado</li><li>Beans<br>(Borlotti, Butter, Green)</li><li>Beetroot</li><li>Bokchoy</li><li>Broccoli</li><li>Brussels Sprouts</li><li>Cabbage</li><li>Capsicum</li><li>Carrot</li><li>Cauliflower</li><li>Celery</li><li>Choko</li><li>Corn</li><li>Cucumber</li><li>Daikon</li><li>Eggplant</li><li>Fennel</li><li>Leek</li><li>Lettuce</li><li>Mushroom<br>(Field, Pine,<br>Slippery Jacks)</li><li>Okra</li><li>Onion</li><li>Onion Spring</li><li>Parsnip</li><li>Peas</li><li>Potato</li>
      </ul>
      <ul class="items" style="left:296px;top:37px">
        <li>Pumpkin</li><li>Radish</li><li>Shallot</li><li>Silverbeet</li><li>Spinach</li><li>Squash</li><li>Swede</li><li>Sweet Potato</li><li>Tomato</li><li>Turnip</li><li>Watercress</li><li>Witlof</li><li>Zucchini</li>
      </ul>
    </div>
    <div class="box box--mint" style="left:600px;top:2343px;width:219px;height:419px">
      <h2 class="box-title box-title--tight" style="left:12px">Herbs &amp; Spices</h2>
      <ul class="items" style="left:52px;top:26px">
        <li>Basil</li><li>Chervil</li><li>Chilli</li><li>Chives</li><li>Coriander</li><li>Dill</li><li>Ginger</li><li>Lime, Kaffir (Leaves)</li><li>Lemongrass</li><li>Mint</li><li>Oregano</li><li>Parsley</li><li>Rosemary</li><li>Sage</li><li>Tarragon</li><li>Thyme</li>
      </ul>
    </div>
    <svg class="season-word" style="left:876px;top:1991px" width="229" height="771" aria-label="Autumn">
      <text transform="rotate(90)" x="0" y="-14" textLength="771" lengthAdjust="spacingAndGlyphs">AUTUMN</text>
    </svg>
    <div class="month month--autumn" style="left:977px;top:2010px;width:46px;height:162px">March</div>
    <div class="month month--autumn" style="left:977px;top:2305px;width:46px;height:172px">April</div>
    <div class="month month--autumn" style="left:977px;top:2610px;width:46px;height:152px">May</div>

    <div class="produce produce--tomato" style="left:67px;top:2800px;width:381px;height:162px" role="img" aria-label="Photo of ripe red tomatoes"></div>
    <div class="produce produce--orange" style="left:486px;top:2800px;width:352px;height:162px" role="img" aria-label="Photo of mandarins with leaves"></div>
    <div class="produce produce--onion" style="left:867px;top:2790px;width:257px;height:172px" role="img" aria-label="Photo of brown onions"></div>
  </section>

  <!-- Winter -->
  <section class="season season--winter">
    <svg class="season-word" style="left:105px;top:3000px" width="219" height="677" aria-label="Winter">
      <text transform="rotate(-90)" x="-677" y="213" textLength="677" lengthAdjust="spacingAndGlyphs">WINTER</text>
    </svg>
    <div class="month month--winter month--up" style="left:187px;top:3006px;width:48px;height:137px">June</div>
    <div class="month month--winter month--up" style="left:187px;top:3238px;width:48px;height:172px">July</div>
    <div class="month month--winter month--up" style="left:187px;top:3534px;width:48px;height:143px">August</div>

    <div class="box box--mint" style="left:368px;top:3000px;width:246px;height:676px">
      <h2 class="box-title box-title--tight">Fruits</h2>
      <ul class="items" style="left:57px;top:38px">
        <li>Avocado</li><li>Cumquat</li><li>Custard Apple</li><li>Feijoa</li><li>Grapefruit</li><li>Kiwi Fruit</li><li>Lemon</li><li>Lime</li><li>Mandarin<br>(Ellendale, Imperial,<br>Murcot)</li><li>Orange<br>(Blood, Navel, Seville)</li><li>Pear Nashi</li><li>Persimmon</li><li>Pineapple</li><li>Quince</li><li>Rhubarb</li><li>Tamarillo</li><li>Tangelo</li>
      </ul>
    </div>
    <div class="box box--cream veg--winter" style="left:634px;top:3000px;width:474px;height:676px">
      <h2 class="box-title box-title--tight">Vegetables</h2>
      <ul class="items" style="left:65px;top:38px">
        <li>Asian Greens<br>( Bok Choy, Choy Sum,<br>Gai Laan, Wombok)</li><li>Beetroot</li><li>Broccoli</li><li>Broccolini</li><li>Beans, Broad</li><li>Brussels Sprouts</li><li>Cabbage</li><li>Carrot</li><li>Cauliflower</li><li>Celeriac</li><li>Celery</li><li>Chokos</li><li>Fennel</li><li>Horseradish</li><li>Kale</li><li>Kohlrabi</li><li>Leek</li><li>Lettuce</li><li>Mushrooms</li><li>Okra</li><li>Onion</li>
      </ul>
      <ul class="items" style="left:288px;top:38px">
        <li>Onion, Spring</li><li>Parsnip</li><li>Peas</li><li>Peas, Snow</li><li>Potato</li><li>Pumpkin</li><li>Radish</li><li>Shallot</li><li>Silverbeet</li><li>Spinach</li><li>Swede</li><li>Sweet Potato</li><li>Turnip</li>
      </ul>
    </div>
    <div class="box box--mint" style="left:891px;top:3429px;width:217px;height:248px">
      <h2 class="box-title box-title--tight" style="left:16px;top:20px">Herbs &amp; Spices</h2>
      <ul class="items items--roomy" style="left:67px;top:22px">
        <li>Ginger</li><li>Coriander</li><li>Dill</li><li>Mint</li><li>Oregano</li><li>Parsley</li><li>Rosemary</li>
      </ul>
    </div>
    <div class="produce produce--broccoli" style="left:57px;top:3560px;width:419px;height:340px" role="img" aria-label="Photo of a broccoli head"></div>
    <div class="produce produce--beet" style="left:743px;top:3715px;width:400px;height:209px" role="img" aria-label="Photo of beetroot with leaves"></div>
  </section>

  <!-- Spring -->
  <section class="season season--spring">
    <div class="box box--mint" style="left:105px;top:3943px;width:229px;height:876px">
      <h2 class="box-title">Fruits</h2>
      <ul class="items" style="left:53px;top:21px">
        <li>Asparagus</li><li>Avocado</li><li>Banana</li><li>Blueberries<br>(Start Of Nov.)</li><li>Cantaloupe</li><li>Cherry</li><li>Cumquat</li><li>Grapefruit</li><li>Honeydew</li><li>Kiwi Fruit</li><li>Lemon</li><li>Lime</li><li>Loquat</li><li>Lychee</li><li>Mandarin<br>(Ellendale, Imperial<br>Murcot)</li><li>Mango</li><li>Mulberries</li><li>Orange<br>(Blood, Seville,<br>Valencia)</li><li>Papaya</li><li>Pear Corella</li><li>Pepino</li><li>Pineapple</li><li>Rhubarb</li><li>Strawberries</li><li>Starfruit</li><li>Tangelo</li><li>Watermelon</li>
      </ul>
    </div>
    <div class="box box--cream veg--spring" style="left:352px;top:3943px;width:471px;height:876px">
      <h2 class="box-title">Vegetables</h2>
      <ul class="items" style="left:77px;top:21px">
        <li>Artichoke<br>(Globe, Jerusalem)</li><li>Asian Greens<br>(Bok Choy, Choy Sum,<br>Gai Laan, Wombok)</li><li>Beans<br>(Broad, Green)</li><li>Beetroot</li><li>Broccoli</li><li>Brussels Sprouts</li><li>Cabbage</li><li>Capsicum</li><li>Carrot</li><li>Cauliflower</li><li>Celery</li><li>Choko</li><li>Corn</li><li>Cucumber</li><li>Daikon</li><li>Eggplant</li><li>Fennel</li><li>Leek</li><li>Lettuce</li><li>Mushrooms</li><li>Okra</li><li>Onion</li><li>Onion, Spring</li><li>Parsnip</li><li>Peas</li><li>Potato</li><li>Pumpkin</li><li>Radish</li>
      </ul>
      <ul class="items" style="left:290px;top:21px">
        <li>Shallot</li><li>Silverbeet</li><li>Spinach</li><li>Squash</li><li>Swede</li><li>Sweet Potato</li><li>Tomato</li><li>Turnip</li><li>Watercress</li><li>Witlof</li><li>Zucchini</li>
      </ul>
    </div>
    <div class="box box--mint" style="left:610px;top:4286px;width:213px;height:533px">
      <h2 class="box-title" style="left:16px;top:30px">Herbs &amp; Spices</h2>
      <ul class="items items--herbs-spring" style="left:74px;top:32px">
        <li>Basil</li><li>Chervil</li><li>Chilli</li><li>Chives</li><li>Coriander</li><li>Dill</li><li>Garlic</li><li>Ginger</li><li>Lime, Kaffir<br>(Leaves)</li><li>Lemongrass</li><li>Mint</li><li>Oregano</li><li>Parsley</li><li>Rosemary</li><li>Sage</li><li>Tarragon</li><li>Thyme</li>
      </ul>
    </div>
    <svg class="season-word" style="left:876px;top:3953px" width="229" height="867" aria-label="Spring">
      <text transform="rotate(90)" x="0" y="-14" textLength="867" lengthAdjust="spacingAndGlyphs">SPRING</text>
    </svg>
    <div class="month month--spring" style="left:977px;top:3972px;width:46px;height:219px">September</div>
    <div class="month month--spring" style="left:977px;top:4248px;width:46px;height:191px">October</div>
    <div class="month month--spring" style="left:977px;top:4553px;width:46px;height:229px">November</div>

    <div class="produce produce--chilli" style="left:838px;top:4153px;width:172px;height:86px" role="img" aria-label="Photo of a red chilli"></div>
    <div class="produce produce--cherry" style="left:724px;top:4690px;width:209px;height:170px" role="img" aria-label="Photo of a pair of cherries"></div>
  </section>

  <footer>
    <p class="footer-url">WWW.CRISPHARVEST.COM.AU</p>
    <div class="social">
      <div>@thecrispharvest<span class="social-dot"></span></div>
      <div>The Crisp Harvest Co</div>
    </div>
  </footer>
</main>
</body>
</html>
```